Nutrition business needs logo & business card design

We need a business card & logo design for a new company based in Toronto, Ontario Canada called Verdin Wellcraft.

We provide nutrition service using metrics as guide to manage client's progress. Our service creates individualized nutrition and lifestyle strategies that focuses on improving Performance, Longevity and Weight Loss. I would like to see designs that use the color of green, gray, blue and white.

The final design should:

--convey a feeling of connectedness with positive transformation.

-- communicate the idea of awareness with guided effort that yields personal independence for a better and more productive life

Target Market(s)

Professionals who work in the IT/Computer/Engineering/Banking industry specifically Directors, Managers, CEO's.

Industry/Entity Type

Health And Wellness

Contact Information for Business Card

Morvessa Dunt, Owner
email: MDUNT@verdinwellcraft.example
tel: - 416-555-0147

Logo Text

better health through analytics or measure to manage

Font styles to use
Other font styles liked:
• Garamound

Colors
ffffff
abd037
85acd3
757575
34a7d7

Requirements
Must have
• Good contrast and decent size font - ease of readability, aesthetically nice colors
Nice to have
• image of chart or graph that conveys measurement or analytics
Should not have
• Borders, images of food,

```html
<!DOCTYPE html>
<html lang="en">
<head>
<meta charset="utf-8">
<title>Verdin Wellcraft — Business Card</title>
<link rel="stylesheet" href="https://fonts.googleapis.com/css2?family=EB+Garamond:wght@400;600&display=swap">
<style>
  :root {
    --backdrop: #1c1c1d;
    --card-dark: #302f31;
    --card-light: #ffffff;
    --accent-green: #abd037;
    --text-light: #ececec;
    --text-brand: #333333;
    --rule-dark: #1f1e20;
    --rule-light: #4a494c;
  }
  html, body {
    margin: 0;
    padding: 0;
    width: 1200px;
    height: 757px;
    overflow: hidden;
    background: var(--backdrop);
  }
  .canvas {
    position: relative;
    width: 1200px;
    height: 757px;
  }
  .business-card {
    position: absolute;
    left: 120px;
    top: 104px;
    width: 960px;
    height: 548px;
    background: var(--card-dark);
    overflow: hidden;
    font-family: "EB Garamond", Garamond, "Times New Roman", serif;
    box-shadow: 0 12px 30px rgba(0,0,0,0.45);
  }
  .card-shapes {
    position: absolute;
    inset: 0;
  }
  .contact-block {
    position: absolute;
    left: 100px;
    top: 0;
    width: 360px;
  }
  .holder-name {
    position: absolute;
    left: 10px;
    top: 236px;
    margin: 0;
    font-size: 27px;
    font-weight: 400;
    color: var(--text-light);
    white-space: nowrap;
  }
  .holder-role {
    position: absolute;
    left: 10px;
    top: 270px;
    margin: 0;
    font-size: 23px;
    color: var(--accent-green);
  }
  .contact-rule {
    position: absolute;
    left: 0;
    width: 340px;
    height: 1px;
    background: var(--rule-dark);
    box-shadow: 0 1px 0 var(--rule-light);
  }
  .rule-upper { top: 316px; }
  .rule-lower { top: 376px; left: 12px; }
  .contact-phone,
  .contact-email {
    position: absolute;
    left: 18px;
    margin: 0;
    font-size: 25px;
    color: var(--text-light);
    white-space: nowrap;
  }
  .contact-phone { top: 330px; }
  .contact-email { top: 392px; left: 28px; }
  .brand-block {
    position: absolute;
    left: 620px;
    top: 170px;
    width: 320px;
    text-align: center;
  }
  .brand-dot {
    display: block;
    width: 84px;
    height: 84px;
    margin: 0 auto 26px;
    border-radius: 50%;
    background: var(--accent-green);
  }
  .brand-name {
    margin: 0;
    font-size: 31px;
    font-weight: 600;
    color: var(--text-brand);
    white-space: nowrap;
  }
</style>
</head>
<body>
<main class="canvas">
  <section class="business-card" aria-label="Verdin Wellcraft business card">
    <svg class="card-shapes" width="960" height="548" viewBox="0 0 960 548" aria-hidden="true">
      <g class="icon-tabs">
        <rect x="440" y="238" width="170" height="50" fill="var(--accent-green)"/>
        <rect x="440" y="292" width="170" height="50" fill="var(--accent-green)"/>
        <rect x="440" y="346" width="170" height="50" fill="var(--accent-green)"/>
      </g>
      <g class="tab-icon icon-person" fill="#ffffff">
        <circle cx="478" cy="254" r="8"/>
        <path d="M463 280 q0 -14 15 -14 q15 0 15 14 z"/>
      </g>
      <g class="tab-icon icon-phone" fill="#ffffff">
        <path d="M464 311 q14 -8 28 0 l-2 5 h-6 v-3 q-6 -2 -12 0 v3 h-6 z"/>
        <rect x="467" y="318" width="22" height="12" rx="2"/>
      </g>
      <g class="tab-icon icon-monitor">
        <rect x="465" y="359" width="28" height="18" rx="1" fill="none" stroke="#ffffff" stroke-width="3"/>
        <rect x="476" y="377" width="6" height="5" fill="#ffffff"/>
        <rect x="470" y="382" width="18" height="3" fill="#ffffff"/>
      </g>
      <polygon class="light-panel" points="420,0 960,0 960,548 640,548" fill="var(--card-light)"/>
    </svg>

    <div class="contact-block">
      <p class="holder-name">Morvessa Dunt</p>
      <p class="holder-role">Owner</p>
      <span class="contact-rule rule-upper"></span>
      <p class="contact-phone">416-555-0147</p>
      <span class="contact-rule rule-lower"></span>
      <p class="contact-email">MDUNT@verdinwellcraft.example</p>
    </div>

    <div class="brand-block">
      <span class="brand-dot"></span>
      <p class="brand-name">Verdin Wellcraft</p>
    </div>
  </section>
</main>
</body>
</html>
```